Webdesign für Ein traditionsreicher & moderner Handwerksbetrieb
Zielgruppe
Werbeagentur sucht Designer für Handwerker-Website
Aufgabenstellung
Es wird ein frisches, innovatives Design benötigt, das das Dachdeckerhandwerk adäquat repräsentiert. Außerdem soll es eine gewisse Kapazität, Professionalität und Seriosität widerspiegeln.

```html
<!DOCTYPE html>
<html lang="en">
<head>
<meta charset="utf-8">
<title>Roofing – Startseite</title>
<link href="https://fonts.googleapis.com/css2?family=Source+Sans+3:wght@300;400;600;700&display=swap" rel="stylesheet">
<style>
:root{
  --brown:#7a6556;
  --brown-dark:#6b5546;
  --beige:#eedac1;
  --text:#8a8a8a;
  --white:#ffffff;
  --line:#c9b296;
  --accent-quote:#e3c9aa;
}
*{margin:0;padding:0;box-sizing:border-box}
html,body{width:1200px;height:2427px;overflow:hidden}
body{position:relative;font-family:"Source Sans 3",sans-serif;color:var(--text);background:var(--white)}
.abs{position:absolute}
.nav{left:0;top:0;width:1200px;height:63px;background:var(--brown)}
.brand{left:100px;top:6px;font-size:38px;font-weight:600;color:var(--white);letter-spacing:.5px}
.nav-link{top:22px;font-size:14px;font-weight:700;letter-spacing:1px;color:var(--white)}
.nav-active{left:427px;top:14px;width:110px;height:32px;background:var(--beige);border-radius:3px;color:var(--brown-dark);font-size:14px;font-weight:700;letter-spacing:1px;text-align:center;line-height:32px}
.hero{left:0;top:63px;width:1200px;height:547px;background:linear-gradient(120deg,#e9e6e2 0%,#d8d2cb 35%,#8a7f76 60%,#5d6b48 85%,#c8c4bd 100%)}
.hero-title{left:100px;top:408px;font-size:40px;font-weight:700;color:var(--brown-dark)}
.hero-sub{left:100px;top:452px;width:440px;font-size:23px;line-height:28px;color:var(--brown-dark)}
.dot{top:585px;width:15px;height:15px;border-radius:50%;background:#3a3a3a}
.h-section{font-size:22px;font-weight:700;color:var(--brown-dark)}
.body-text{font-size:15px;line-height:25px;text-align:justify;font-weight:300;color:var(--text)}
.intro-text{font-size:16px;letter-spacing:-.3px;font-weight:400;color:#959595}
.more{left:100px;top:978px;font-size:13px;font-weight:600;color:var(--brown-dark);text-decoration:underline}
.checks{left:824px;top:705px;list-style:none}
.checks li{display:flex;align-items:center;height:34px;font-size:20px;color:#9a9a9a}
.checks svg{margin-right:16px}
.featured{left:0;top:1060px;width:1200px;height:637px;background:var(--beige)}
.rule{height:1px;background:var(--line)}
.title-big{font-size:30px;font-weight:700;color:var(--brown-dark);text-align:center;width:1200px;left:0}
.title-sub{font-size:22px;color:var(--brown-dark);text-align:center;width:1200px;left:0}
.card{top:1182px;width:238px;height:403px;background:var(--white);border-radius:3px}
.card-img{position:absolute;left:8px;top:8px;width:222px;height:217px}
.card-title{position:absolute;left:0;top:236px;width:238px;text-align:center;font-size:14px;font-weight:400;line-height:19px;color:var(--brown-dark);letter-spacing:.3px}
.card-rule{position:absolute;left:8px;top:283px;width:222px;height:1px;background:var(--brown-dark)}
.card-text{position:absolute;left:8px;top:291px;width:222px;font-size:16px;letter-spacing:-.3px;font-weight:400;color:#9a9a9a}
.btn{left:517px;top:1622px;width:176px;height:50px;border:2px solid var(--brown-dark);border-radius:5px;font-size:18px;color:var(--brown-dark);text-align:center;line-height:46px}
.person{left:120px;top:1815px;width:335px;height:353px;background:radial-gradient(ellipse at 50% 30%,#dcd2c8 0%,#c6d7ec 55%,#a9c2e0 100%);border-radius:160px 160px 0 0}
.quote-mark{font-size:90px;font-weight:700;color:var(--accent-quote);line-height:1}
.quote-text{left:545px;top:1867px;width:447px;font-size:16px;letter-spacing:-.2px;font-weight:400;color:#959595}
.client{left:543px;top:2080px;font-size:22px;font-weight:600;color:var(--brown-dark)}
.footer{left:0;top:2178px;width:1200px;height:249px;background:var(--brown)}
.f-head{top:2198px;font-size:16px;font-weight:700;letter-spacing:.5px;color:var(--beige)}
.f-text{font-size:16px;line-height:25px;color:var(--white);letter-spacing:-.2px}
.f-input{left:100px;top:2306px;width:165px;height:34px;background:var(--white);border:1px solid #ccc;font-size:13px;color:#777;padding:8px 7px}
.f-btn{left:100px;top:2355px;width:103px;height:29px;background:var(--beige);color:var(--brown-dark);font-size:13px;font-weight:700;text-align:center;line-height:29px;border-radius:2px}
.social{top:2348px;width:23px;height:23px;border-radius:3px}
</style>
</head>
<body>
<header class="abs nav">
  <div class="abs brand">Roofing</div>
  <div class="abs nav-active">STARTSEITE</div>
  <div class="abs nav-link" style="left:560px">LEISTUNGEN</div>
  <div class="abs nav-link" style="left:697px">ÜBER UNS</div>
  <div class="abs nav-link" style="left:807px">REFERENZEN</div>
  <div class="abs nav-link" style="left:940px">NEWS</div>
  <div class="abs nav-link" style="left:1033px">KONTAKT</div>
</header>

<section class="abs hero" role="img" aria-label="Roofer in hard hat working on a roof"></section>
<h1 class="abs hero-title">FULL SERVICE ROOFING</h1>
<p class="abs hero-sub">sheet metal contractor specializing in commercial roofing, industrial roofing and residential roofing.</p>
<span class="abs dot" style="left:573px;background:var(--beige)"></span>
<span class="abs dot" style="left:598px"></span>
<span class="abs dot" style="left:622px"></span>

<h2 class="abs h-section" style="left:98px;top:693px">ROOFING CONTRACTOR SERVING</h2>
<p class="abs body-text intro-text" style="left:100px;top:735px;width:602px">We deliver dependability, longevity and building strength. Ridgeline Roofing Services has a record of success based on years of professional performance. When you select Ridgeline Roofing Services, you're investing in quality-assured construction methods. Also, you get unsurpassed performance and reliability. We stay ahead of the competition through quality and top-notch roofing services.</p>
<p class="abs body-text intro-text" style="left:100px;top:885px;width:602px">We hope you enjoy browsing through our website. Please feel free to contact us on our contact page. Contact us regarding any information, questions, quotes or comments concerning roofing construction or our business.</p>
<a class="abs more">More</a>

<ul class="abs checks">
  <li><svg width="20" height="18" viewBox="0 0 20 18"><rect x="1" y="3" width="14" height="14" fill="none" stroke="#7a6556" stroke-width="2"/><path d="M4 9l4 4 10-12" fill="none" stroke="#7a6556" stroke-width="2.5"/></svg>Shingles</li>
  <li><svg width="20" height="18" viewBox="0 0 20 18"><rect x="1" y="3" width="14" height="14" fill="none" stroke="#7a6556" stroke-width="2"/><path d="M4 9l4 4 10-12" fill="none" stroke="#7a6556" stroke-width="2.5"/></svg>Flat roofs/built-up roofs</li>
  <li><svg width="20" height="18" viewBox="0 0 20 18"><rect x="1" y="3" width="14" height="14" fill="none" stroke="#7a6556" stroke-width="2"/><path d="M4 9l4 4 10-12" fill="none" stroke="#7a6556" stroke-width="2.5"/></svg>Complete re-roofing</li>
  <li><svg width="20" height="18" viewBox="0 0 20 18"><rect x="1" y="3" width="14" height="14" fill="none" stroke="#7a6556" stroke-width="2"/><path d="M4 9l4 4 10-12" fill="none" stroke="#7a6556" stroke-width="2.5"/></svg>Roof repairs</li>
  <li><svg width="20" height="18" viewBox="0 0 20 18"><rect x="1" y="3" width="14" height="14" fill="none" stroke="#7a6556" stroke-width="2"/><path d="M4 9l4 4 10-12" fill="none" stroke="#7a6556" stroke-width="2.5"/></svg>Expert flashing</li>
  <li><svg width="20" height="18" viewBox="0 0 20 18"><rect x="1" y="3" width="14" height="14" fill="none" stroke="#7a6556" stroke-width="2"/><path d="M4 9l4 4 10-12" fill="none" stroke="#7a6556" stroke-width="2.5"/></svg>Insurance claims</li>
  <li><svg width="20" height="18" viewBox="0 0 20 18"><rect x="1" y="3" width="14" height="14" fill="none" stroke="#7a6556" stroke-width="2"/><path d="M4 9l4 4 10-12" fill="none" stroke="#7a6556" stroke-width="2.5"/></svg>Free estimates</li>
  <li><svg width="20" height="18" viewBox="0 0 20 18"><rect x="1" y="3" width="14" height="14" fill="none" stroke="#7a6556" stroke-width="2"/><path d="M4 9l4 4 10-12" fill="none" stroke="#7a6556" stroke-width="2.5"/></svg>Bonded and insured</li>
</ul>

<section class="abs featured"></section>
<div class="abs rule" style="left:100px;top:1121px;width:348px"></div>
<div class="abs rule" style="left:761px;top:1121px;width:340px"></div>
<h2 class="abs title-big" style="top:1090px">FEATURED PROJECTS</h2>
<p class="abs title-sub" style="top:1125px">Our Most Recent Works</p>

<article class="abs card" style="left:92px">
  <div class="card-img" role="img" aria-label="Roofer laying slate tiles" style="background:linear-gradient(180deg,#c9d2d8,#7f95a6)"></div>
  <h3 class="card-title">RECOMMENDED ROOF<br>MAINTENANCE CONTRACTORS</h3><div class="card-rule"></div>
  <p class="card-text body-text">We deliver dependability, longevity and building strength. Ridgeline Roofing Services has a record of success..</p>
</article>
<article class="abs card" style="left:350px">
  <div class="card-img" role="img" aria-label="Roofer sealing flashing by a brick chimney" style="background:linear-gradient(180deg,#9a6f55,#6d6a78 60%,#c6b9a7)"></div>
  <h3 class="card-title">RECOMMENDED ROOF<br>MAINTENANCE CONTRACTORS</h3><div class="card-rule"></div>
  <p class="card-text body-text">We deliver dependability, longevity and building strength. Ridgeline Roofing Services has a record of success..</p>
</article>
<article class="abs card" style="left:609px">
  <div class="card-img" role="img" aria-label="Worker in safety vest on a flat roof" style="background:linear-gradient(180deg,#b4b4b2,#6e6e6c)"></div>
  <h3 class="card-title">RECOMMENDED ROOF<br>MAINTENANCE CONTRACTORS</h3><div class="card-rule"></div>
  <p class="card-text body-text">We deliver dependability, longevity and building strength. Ridgeline Roofing Services has a record of success..</p>
</article>
<article class="abs card" style="left:869px">
  <div class="card-img" role="img" aria-label="Carpenter hammering roof framing against blue sky" style="background:linear-gradient(160deg,#2f6db3,#6c9ad0 60%,#c9925a)"></div>
  <h3 class="card-title">RECOMMENDED ROOF<br>MAINTENANCE CONTRACTORS</h3><div class="card-rule"></div>
  <p class="card-text body-text">We deliver dependability, longevity and building strength. Ridgeline Roofing Services has a record of success..</p>
</article>
<div class="abs btn">Load More</div>

<h2 class="abs title-big" style="top:1729px">CLIENT TESTIMONIALS</h2>
<p class="abs title-sub" style="top:1764px">Our Most Recent Clients</p>
<div class="abs person" role="img" aria-label="Portrait of a smiling client in shirt and tie"></div>
<svg class="abs" style="left:60px;top:1911px" width="40" height="40" viewBox="0 0 40 40"><circle cx="20" cy="20" r="18" fill="none" stroke="#555" stroke-width="2"/><path d="M24 13v14l-11-7z" fill="#555"/></svg>
<svg class="abs" style="left:1099px;top:1911px" width="40" height="40" viewBox="0 0 40 40"><circle cx="20" cy="20" r="18" fill="none" stroke="#555" stroke-width="2"/><path d="M16 13v14l11-7z" fill="#555"/></svg>
<div class="abs quote-mark" style="left:487px;top:1840px">“</div>
<div class="abs quote-mark" style="left:990px;top:2037px">”</div>
<p class="abs body-text quote-text">Lorem ipsum dolor sit amet, consectetuer adipiscing elit. Aenean commodo ligula eget dolor. Aenean massa. Cum sociis natoque penatibus et magnis dis parturient montes, nascetur ridiculus mus. Donec quam felis, ultricies nec, pellentesque eu, pretium quis, sem.Lorem ipsum dolor sit amet, consectetuer adipiscing elit. Aenean commodo ligula eget doloragnis dis parturient montes, nascetur ridiculus mus. Donec quam felis, ultricies nec, pellentesque eu, pretium quis, sem.</p>
<div class="abs client">Aldric</div>

<footer class="abs footer"></footer>
<h4 class="abs f-head" style="left:100px">NEWSLETTER</h4>
<p class="abs f-text" style="left:100px;top:2233px;width:182px;line-height:21px">Subscribe here to receive our free e-newsletters and notifications ...</p>
<div class="abs f-input">Your Email Address</div>
<div class="abs f-btn">SUBSCRIBE</div>
<h4 class="abs f-head" style="left:395px">QUICKLINKS</h4>
<p class="abs f-text" style="left:395px;top:2231px">Startseite<br>Leistungen<br>Über Uns<br>Referenzen<br>News<br>Kontakt</p>
<h4 class="abs f-head" style="left:606px">BUSINESS HOURS</h4>
<p class="abs f-text" style="left:606px;top:2231px">Monday-Friday<br>7 a.m.-5 p.m.</p>
<h4 class="abs f-head" style="left:889px">CONTACT US</h4>
<p class="abs f-text" style="left:889px;top:2231px">Ridgeline Roofing Services<br>Maplewood, Elm Creek &amp; Stonebridge,<br>Westhaven<br>Phone: 555-014-2870</p>
<span class="abs social" style="left:892px;background:#3b5b98"></span>
<span class="abs social" style="left:921px;background:#3fa9e0"></span>
<span class="abs social" style="left:950px;background:#d64533"></span>
<span class="abs social" style="left:979px;background:#2f79b5"></span>
</body>
</html>
```